50th Anniversary Gala Save the date Postcard 8.5x5.5 inches

Looking for a 5.5x8.5 in one-sided postcard design for our annual gala. Design needs to include "Save the date" prominently with all the event information included below. Design should be light, include the colors of our logo and elegant. (almost like a wedding save the date). "Bridges of Grace" should look like its own logo.

50th Anniversary Gala at The Lodge at Birchmere Glen – “Bridges of Grace – Celebrating 50 Years of Building Community”
Thursday, October 24
6-11p
The Lodge at Birchmere Glen
Calloway Parkway, New Hyde Park, NY
Honoring – TRB Previous Presidents

Target Market(s)

Exisiting donors

Industry/Entity Type

nonprofit

Font styles to use
Serif
Script

Requirements
Must have
• Save the date prominent
Should not have
• should not have a dark background

```html
<!DOCTYPE html>
<html lang="en">
<head>
<meta charset="utf-8">
<title>50th Anniversary Gala – Save the Date</title>
<link rel="stylesheet" href="https://fonts.googleapis.com/css2?family=Oswald:wght@300;400;500;600;700&family=Dancing+Script:wght@500;600&family=Great+Vibes&display=swap">
<style>
  :root {
    --page: #efede8;
    --card-white: #ffffff;
    --navy: #1c4985;
    --panel-top: #1f4f8d;
    --panel-bottom: #1a457f;
    --green: #6aa842;
    --gold: #d9a93f;
    --sky: #1b96d9;
  }
  html, body {
    margin: 0;
    width: 1200px;
    height: 1200px;
    overflow: hidden;
    background: var(--page);
  }
  .postcard {
    position: absolute;
    left: 219px;
    width: 761px;
    height: 492px;
    overflow: hidden;
    box-shadow: 0 4px 10px rgba(0,0,0,0.25);
  }
  .postcard--block { top: 73px; }
  .postcard--script { top: 626px; }
  .postcard svg { display: block; }
  .sans { font-family: "Oswald", sans-serif; }
  .script { font-family: "Great Vibes", cursive; }
  .script-small { font-family: "Dancing Script", cursive; }
  .navy { fill: var(--navy); }
  .green { fill: var(--green); }
  .gold { fill: var(--gold); }
  .sky { fill: var(--sky); }
</style>
</head>
<body>

<div class="postcard postcard--block">
  <svg width="761" height="492" viewBox="0 0 761 492">
    <defs>
      <linearGradient id="panelShadeA" x1="0" y1="0" x2="1" y2="1">
        <stop offset="0" stop-color="var(--panel-top)"/>
        <stop offset="1" stop-color="var(--panel-bottom)"/>
      </linearGradient>
    </defs>
    <rect class="date-side" x="0" y="0" width="285" height="492" fill="var(--card-white)"/>
    <rect class="event-panel" role="img" aria-label="Deep blue panel with a soft pattern of scattered translucent dots" x="285" y="0" width="476" height="492" fill="url(#panelShadeA)"/>

    <g class="save-the-date">
      <text class="sans navy" x="270" y="104" text-anchor="end" font-weight="700" font-size="70"><tspan font-size="98">S</tspan>ave</text>
      <text class="script-small green" x="262" y="135" text-anchor="end" font-style="italic" font-size="24">the</text>
      <text class="sans navy" x="270" y="200" text-anchor="end" font-weight="700" font-size="70"><tspan font-size="98">D</tspan>ate</text>
    </g>

    <g class="event-when sans green" font-size="37" font-weight="400" text-anchor="end" letter-spacing="-0.5">
      <text x="268" y="263">Thursday</text>
      <text x="268" y="300">October 24</text>
      <text x="268" y="337">6 - 11 PM</text>
    </g>

    <g class="event-where sans navy" font-size="21" font-weight="400" text-anchor="end">
      <text x="264" y="400">The Lodge at Birchmere Glen</text>
      <text x="264" y="424">Calloway Parkway</text>
      <text x="264" y="448">New Hyde Park, NY</text>
    </g>

    <g class="event-title sans gold" font-weight="600">
      <text x="307" y="88" font-size="46" font-style="italic" font-weight="700">50<tspan font-size="26" dy="-18" font-style="normal">th</tspan></text>
      <text x="307" y="131" font-size="38" letter-spacing="2">Anniversary</text>
      <text x="307" y="173" font-size="38" letter-spacing="2">Gala</text>
    </g>

    <g class="theme sans sky">
      <text x="307" y="266" font-size="55" font-weight="500" letter-spacing="2">Bridges of Grace</text>
      <text x="307" y="304" font-size="22" font-weight="500" letter-spacing="1">Celebrating</text>
      <text x="307" y="339" font-size="22" font-weight="500" letter-spacing="1">50 Years of Building Community</text>
    </g>

    <g class="honorees sans gold" font-size="22" font-weight="500" letter-spacing="1.5">
      <text x="307" y="416">Honoring</text>
      <text x="307" y="448">TRB Previous Presidents</text>
    </g>
  </svg>
</div>

<div class="postcard postcard--script">
  <svg width="761" height="492" viewBox="0 0 761 492">
    <defs>
      <linearGradient id="panelShadeB" x1="0" y1="0" x2="1" y2="1">
        <stop offset="0" stop-color="var(--panel-top)"/>
        <stop offset="1" stop-color="var(--panel-bottom)"/>
      </linearGradient>
    </defs>
    <rect class="date-side" x="0" y="0" width="285" height="492" fill="var(--card-white)"/>
    <rect class="event-panel" role="img" aria-label="Deep blue panel with a soft pattern of scattered translucent dots" x="285" y="0" width="476" height="492" fill="url(#panelShadeB)"/>

    <g class="save-the-date">
      <text class="script navy" x="42" y="108" font-size="50"><tspan font-size="92">S</tspan>ave</text>
      <text class="script-small gold" x="76" y="138" font-size="22">the</text>
      <text class="script navy" x="264" y="196" text-anchor="end" font-size="50"><tspan font-size="92">D</tspan>ate</text>
    </g>

    <g class="event-when sans green" font-size="37" font-weight="500" text-anchor="end" letter-spacing="-0.5">
      <text x="264" y="263">Thursday</text>
      <text x="264" y="303">October 24</text>
      <text x="264" y="343">6 - 11 PM</text>
    </g>

    <g class="event-where sans navy" font-size="21" font-weight="400" text-anchor="end">
      <text x="264" y="394">The Lodge at Birchmere Glen</text>
      <text x="264" y="419">Calloway Parkway</text>
      <text x="264" y="443">New Hyde Park, NY</text>
    </g>

    <g class="event-title sans gold" font-weight="500">
      <text x="317" y="78" font-size="54">50<tspan font-size="28" dy="-22">th</tspan></text>
      <text x="317" y="134" font-size="54">Anniversary</text>
      <text x="317" y="188" font-size="54">Gala</text>
    </g>

    <g class="theme sans sky">
      <text x="317" y="280" font-size="60" font-weight="500" letter-spacing="2">Bridges of Grace</text>
      <text x="317" y="315" font-size="22" font-weight="500" letter-spacing="1">Celebrating</text>
      <text x="317" y="350" font-size="22" font-weight="500" letter-spacing="1">50 Years of Building Community</text>
    </g>

    <g class="honorees sans gold" font-size="22" font-weight="500" letter-spacing="1.5">
      <text x="317" y="412">Honoring</text>
      <text x="317" y="443">TRB Previous Presidents</text>
    </g>
  </svg>
</div>

</body>
</html>
```